Stationery Required - Own Logo provided

Hi,

We are a retail company called 'Copperfinch Trading Limited' based in the UK and would like some corporate stationery designed.

We have provided our Logo which we would like to use (Its attached to this brief)...

The designs must be orginal, professional, stylish and interesting!

Target Market(s)

We will use this stationery to communicate with our wholesale suppliers and employees, so it must have a 'professional' feel about it.

Industry/Entity Type

It Company

Requirements
Must have
• Must be professional, corporate, stylish and not to 'fussy'. we require ... Business card design, a4 letter, compliment slip. All designs must be supplied in a format where the text (address/telephone numbers etc..) can be edited, as we have alot of staff and operate out of several different premises.
Nice to have
• I would like a windows backround picture file supplied as well so we can integrate that onto our computer systems.

```html
<!DOCTYPE html>
<html lang="en">
<head>
<meta charset="utf-8">
<title>Copperfinch Trading Limited – Stationery</title>
<link href="https://fonts.googleapis.com/css2?family=Arimo:wght@400;700&family=Questrial&display=swap" rel="stylesheet">
<style>
  :root{
    --bg:#e8e5e0;
    --paper:#ffffff;
    --green:#8dc63f;
    --green-light:#a9d86e;
    --ink:#3b3b3b;
    --muted:#6d6d6d;
    --faint:#f1f1f1;
  }
  *{box-sizing:border-box;margin:0;padding:0}
  html,body{width:1200px;height:900px;overflow:hidden;background:var(--bg)}
  body{position:relative;font-family:"Arimo",Arial,sans-serif;color:var(--ink)}
  .sheet{position:absolute;background:var(--paper);overflow:hidden}
  .corner-stripes{position:absolute;width:60px;height:60px}
  .brand{font-family:"Questrial",sans-serif;font-weight:400;color:var(--green);letter-spacing:.5px;line-height:1.05}
  .bullet-list{list-style:none}
  .bullet-list li{position:relative;padding-left:16px}
  .bullet-list li::before{content:"";position:absolute;left:2px;top:50%;transform:translateY(-50%);
    border-left:6px solid var(--green);border-top:4px solid transparent;border-bottom:4px solid transparent}

  /* business card – back */
  .card-back{left:180px;top:70px;width:310px;height:500px;background:var(--green)}
  .card-back .brand{position:absolute;left:40px;top:225px;color:#fff;font-size:36px;white-space:nowrap}

  /* business card – front */
  .card-front{left:46px;top:26px;width:310px;height:510px}
  .card-front .brand{position:absolute;left:0;right:0;top:84px;text-align:center;font-size:22px}
  .card-front .person{position:absolute;left:22px;top:282px;font-size:21px;color:var(--ink)}
  .card-front .person strong{color:var(--green);font-weight:400}
  .card-front .person .role{font-size:12px;color:var(--muted);border-left:1px solid var(--green);padding-left:5px;margin-left:5px}
  .card-front .contact{position:absolute;left:22px;top:330px;font-size:13px;line-height:26px;color:var(--muted)}
  .card-front .contact b{color:var(--ink);display:inline-block;width:58px}
  .card-front .address{position:absolute;right:14px;bottom:14px;font-size:10px;color:var(--muted)}

  /* letterhead */
  .letterhead{left:556px;top:26px;width:592px;height:854px}
  .letterhead .address{position:absolute;left:18px;top:28px;font-size:11.5px;line-height:17px;color:var(--muted)}
  .letterhead .brand{position:absolute;right:50px;top:46px;font-size:26px;text-align:right}
  .letterhead .watermark{position:absolute;left:184px;top:290px;width:226px;height:226px;background:var(--faint)}
  .letterhead .base-band{position:absolute;left:0;right:0;bottom:0;height:26px;background:var(--green)}

  /* compliment slip */
  .comp-slip{left:48px;top:584px;width:694px;height:230px}
  .comp-slip .address{position:absolute;left:14px;top:20px;font-size:11.5px;line-height:15px;color:var(--muted)}
  .comp-slip .brand{position:absolute;right:70px;top:30px;font-size:26px;text-align:right}
  .comp-slip .sign-off{position:absolute;right:28px;bottom:30px;font-size:20px;font-weight:700;color:var(--green-light)}
</style>
</head>
<body>

<section class="sheet card-back" aria-label="Business card back">
  <div class="brand">Copperfinch Trading</div>
  <svg class="corner-stripes" style="right:0;top:0" viewBox="0 0 60 60"><g stroke="#fff" stroke-width="3" opacity=".7"><line x1="20" y1="0" x2="60" y2="40"/><line x1="30" y1="0" x2="60" y2="30"/><line x1="40" y1="0" x2="60" y2="20"/></g></svg>
</section>

<section class="sheet card-front" aria-label="Business card front">
  <svg class="corner-stripes" style="right:0;top:0" viewBox="0 0 60 60"><g stroke="#8dc63f" stroke-width="3" opacity=".55"><line x1="20" y1="0" x2="60" y2="40"/><line x1="30" y1="0" x2="60" y2="30"/><line x1="40" y1="0" x2="60" y2="20"/></g></svg>
  <div class="brand">Copperfinch<br>Trading Limited</div>
  <p class="person">Owen<strong>Marsh</strong><span class="role">company director</span></p>
  <ul class="bullet-list contact">
    <li><b>mobile</b>07700900461</li>
    <li><b>e-mail</b>hello@copperfinch.co.uk</li>
  </ul>
  <svg class="corner-stripes" style="left:0;bottom:0" viewBox="0 0 60 60"><g stroke="#8dc63f" stroke-width="3" opacity=".55"><line x1="0" y1="20" x2="40" y2="60"/><line x1="0" y1="30" x2="30" y2="60"/><line x1="0" y1="40" x2="20" y2="60"/></g></svg>
  <p class="address">17 mill brook lane, Ballyroan, County Down BT30 4QP.</p>
</section>

<section class="sheet letterhead" aria-label="Letterhead">
  <svg class="corner-stripes" style="right:0;top:0" viewBox="0 0 60 60"><g stroke="#8dc63f" stroke-width="3" opacity=".55"><line x1="20" y1="0" x2="60" y2="40"/><line x1="30" y1="0" x2="60" y2="30"/><line x1="40" y1="0" x2="60" y2="20"/></g></svg>
  <ul class="bullet-list address">
    <li>17 mill brook lane,</li>
    <li>Ballyroan, County Down</li>
    <li>BT30 4QP</li>
  </ul>
  <div class="brand">Copperfinch<br>Trading Limited</div>
  <div class="watermark" aria-hidden="true"></div>
  <div class="base-band"></div>
</section>

<section class="sheet comp-slip" aria-label="Compliment slip">
  <svg class="corner-stripes" style="right:0;top:0" viewBox="0 0 60 60"><g stroke="#8dc63f" stroke-width="3" opacity=".55"><line x1="20" y1="0" x2="60" y2="40"/><line x1="30" y1="0" x2="60" y2="30"/><line x1="40" y1="0" x2="60" y2="20"/></g></svg>
  <p class="address">17 mill brook lane,<br>Ballyroan, County Down<br>BT30 4QP</p>
  <div class="brand">Copperfinch<br>Trading Limited</div>
  <p class="sign-off">With Compliments</p>
</section>

</body>
</html>
```